cartNest - a stylish trolley for apartments

We neede a simple website to sell our Trolley, for apartment use.
The colour theme is red, blask & white. Our logo is attached and this needs to be on the Home page.
The website only needs a Home Page plus 4 other pges.
In the attachment you will find a site map.

You can check out the following two sites to see what I like:
www.plinvex.example/design-showcase-inspiration/minimalist-portfolio-website/
www.brostaquill.example/inspiration/40-beautiful-web-design-portfolios/ in this site especially
Dario Pesqueta
Q L Smithy
Nine 86 Studio
Albert Crisp

And especially Lamp - I ike the simpicity of the site esp as we are only selling one product

Target Market(s)

Apartment dwellers

Industry/Entity Type

Apartment

Requirements
Must have
• This website must have 4 pages.
We need Zanto, Fundline and Quibpay portals.
Order Form for Trolley
Payment form.

```html
<!DOCTYPE html>
<html lang="en">
<head>
<meta charset="utf-8">
<title>cartNest – a stylish trolley for apartments</title>
<link href="https://fonts.googleapis.com/css2?family=Arimo:wght@400;700&family=Roboto+Condensed:wght@400;700&display=swap" rel="stylesheet">
<style>
:root{
  --dark:#1c1c1c;
  --dark-2:#262626;
  --red:#c4000b;
  --red-deep:#a0000a;
  --paper:#f3f3f3;
  --panel:#e6e5df;
  --ink:#1a1a1a;
  --muted:#555;
  --foot-text:#d8d8d8;
  --foot-dim:#6c6c6c;
}
*{margin:0;padding:0;box-sizing:border-box}
html,body{width:1105px;height:1200px;overflow:hidden}
body{position:relative;background:var(--paper);font-family:"Arimo",Arial,sans-serif;color:var(--ink)}
.site-header{position:absolute;left:0;top:0;width:1105px;height:187px;background:linear-gradient(180deg,#2a2a2a,#141414)}
.brand{position:absolute;left:42px;top:128px;display:flex;align-items:center;gap:10px}
.brand-mark{width:22px;height:22px;background:var(--red)}
.brand-name{font-weight:700;font-size:34px;color:#fff;letter-spacing:-.5px}
.hotline{position:absolute;right:36px;top:48px;display:flex;align-items:center;gap:10px}
.hotline-num{font-family:"Roboto Condensed",sans-serif;font-weight:700;font-size:32px;color:#cfcfcf}
.hero-photo{position:absolute;left:25px;top:187px;width:598px;height:450px;
  background:linear-gradient(90deg,#d9d9d9 0%,#f2f2f2 20%,#bdbdbd 45%,#a9a9a9 70%,#dcdcdc 100%)}
.hero-photo::after{content:"";position:absolute;left:0;right:0;bottom:0;height:140px;background:linear-gradient(180deg,rgba(243,243,243,0),var(--paper))}
.showcase{position:absolute;left:622px;top:157px;width:456px;height:468px;background:var(--panel);border:3px solid #fff;border-radius:8px;box-shadow:0 0 6px rgba(0,0,0,.3)}
.main-nav{position:absolute;left:5px;top:4px;display:flex;justify-content:space-between;align-items:stretch;height:50px;width:444px;padding-right:8px;background:#fff;border-radius:6px 6px 0 0;white-space:nowrap}
.main-nav a{font-family:"Roboto Condensed",sans-serif;font-size:25px;line-height:28px;color:var(--ink);text-decoration:none;padding-top:12px;text-transform:uppercase;white-space:nowrap}
.main-nav a.active{background:var(--red);color:#fff;border-radius:6px 6px 0 0;padding:12px 16px 0}
.feature-slide{position:absolute;left:14px;top:88px;width:426px;height:232px;border:8px solid var(--red);border-radius:4px;
  background:linear-gradient(90deg,#7d7068,#cabfb4 40%,#a48d7a 70%,#9e1212)}
.thumbs{position:absolute;left:8px;top:336px;display:flex;gap:10px}
.thumb{width:138px;height:123px;border:2px solid #fff}
.thumb.t1{background:linear-gradient(135deg,#c9a659,#4a3a2c 60%,#8a1a1a)}
.thumb.t2{background:linear-gradient(135deg,#b49a60,#2d3a6a 60%,#5a4c3a)}
.thumb.t3{background:linear-gradient(135deg,#a7b3bf,#d7dde2 60%,#8c96a0)}
.latest-news{position:absolute;left:630px;top:630px;width:442px;height:282px;background:var(--panel);padding:16px 10px 0}
.latest-news h2{font-weight:400;font-size:20px;color:var(--red-deep);margin:0 0 16px 14px}
.news-item{margin-bottom:18px}
.news-date{display:flex;align-items:center;gap:10px;font-size:13px;line-height:19px;color:#333;margin-bottom:2px}
.news-item p{font-size:12.8px;line-height:19px;color:#333;white-space:nowrap;letter-spacing:-.1px;overflow:hidden}
.welcome{position:absolute;left:24px;top:668px;width:600px;height:240px;overflow:hidden}
.welcome h1{font-weight:400;font-size:20px;margin-bottom:16px}
.welcome h1 .title-lead{text-decoration:underline;text-underline-offset:4px}
.welcome h1 .title-brand{color:var(--red);font-weight:700;margin-left:6px}
.welcome p{font-size:13.3px;line-height:20px;color:var(--muted)}
.welcome p strong{color:var(--red);font-size:16px}
.site-footer{position:absolute;left:0;top:927px;width:1105px;height:248px;background:linear-gradient(180deg,var(--dark-2),var(--dark))}
.foot-col{position:absolute;top:22px}
.foot-col h3{font-size:13.5px;color:#fff;margin-bottom:24px}
.testimonial p{font-size:13.3px;line-height:20px;color:var(--foot-dim)}
.testimonial cite{display:block;text-align:right;font-style:normal;font-size:13.3px;color:var(--foot-text);margin:3px 30px 22px 0}
.divider{position:absolute;top:42px;width:1px;height:150px;background:#444}
.cards{display:flex;gap:16px;margin-bottom:30px}
.card{width:38px;height:20px;border-radius:2px}
.action{display:flex;gap:14px;align-items:flex-start;margin-bottom:22px;font-size:13.3px;line-height:20px;color:var(--foot-text)}
.action a{color:#fff}
.contact-row{display:flex;align-items:center;gap:12px;font-size:13.3px;line-height:20px;color:var(--foot-text);margin-bottom:24px}
.contact-row a{color:#f0a9a9}
.contact-phone{font-family:"Roboto Condensed",sans-serif;font-weight:700;font-size:21px;color:#fff}
.copyright{position:absolute;left:0;top:1175px;width:1105px;height:25px;background:#e9e9e4;text-align:center;font-size:13.3px;line-height:25px}
</style>
</head>
<body>
<header class="site-header">
  <div class="brand"><span class="brand-mark"></span><span class="brand-name">cartNest</span></div>
  <div class="hotline">
    <svg width="54" height="54" viewBox="0 0 54 54" aria-hidden="true"><circle cx="27" cy="27" r="25" fill="#e0a21a"/><path d="M18 20c3-4 15-4 18 0l-3 4h-12z M16 26h22v10H16z" fill="#1c1c1c"/></svg>
    <span class="hotline-num">+014 58210377</span>
  </div>
</header>

<div class="hero-photo" role="img" aria-label="Chrome luggage trolley with red suitcases in front of steel lift doors"></div>

<section class="showcase">
  <nav class="main-nav">
    <a class="active" href="#">Home</a><a href="#">About us</a><a href="#">Contact us</a><a href="#">News</a>
  </nav>
  <div class="feature-slide" role="img" aria-label="Trolley loaded with luggage in a hotel lobby"></div>
  <div class="thumbs">
    <div class="thumb t1" role="img" aria-label="Porter loading bags onto trolley"></div>
    <div class="thumb t2" role="img" aria-label="Porter handing over luggage"></div>
    <div class="thumb t3" role="img" aria-label="Close view of trolley frame"></div>
  </div>
</section>

<section class="welcome">
  <h1><span class="title-lead">WELCOME TO </span><span class="title-brand">cartNest</span></h1>
  <p><strong>cartNest</strong> evolved from demand!&nbsp; Apartment dwellers everywhere are calling for a solution to moving shopping, luggage and other goods from car to apartment, and vice versa. Other trolleys on the market are not versatile, they are not robust, but more importantly, they are NOT stylish! The emphasis of cartNest is on style. This trolley is stylish enough to remain in your apartment as a piece of furniture. It features a versatile flat-bed and hanger, to cope with all your transport needs. cartNest evolved from demand!&nbsp; Apartment dwellers everywhere are calling for a solution to moving shopping, luggage and other goods from car to apartment, and vice versa. Other trolleys on the market are not versatile, they are not robust, but more importantly, they are NOT stylish! The emphasis of cartNest is on style. This trolley is stylish enough to remain in your apartment as a piece of furniture. It features a versatile flat-bed and hanger, to cope with all your transport needs.</p>
</section>

<aside class="latest-news">
  <h2>LATEST NEWS</h2>
  <div class="news-item">
    <div class="news-date"><svg width="22" height="16" aria-hidden="true"><rect x="1" y="1" width="20" height="14" fill="#fff" stroke="#3a5ea8"/><rect x="4" y="4" width="6" height="5" fill="#3a5ea8"/></svg>Date:21 july,2012</div>
    <p>Lorem Ipsum is simply dummy text of the printing and typesetting indus-<br>try&nbsp; Lorem Ipsum is simply dummy text of the printing and typesetting</p>
  </div>
  <div class="news-item">
    <div class="news-date"><svg width="22" height="16" aria-hidden="true"><rect x="1" y="1" width="20" height="14" fill="#fff" stroke="#3a5ea8"/><rect x="4" y="4" width="6" height="5" fill="#3a5ea8"/></svg>Date:21 july,2012</div>
    <p>Lorem Ipsum is simply dummy text of the printing and typesetting indus-<br>try&nbsp; Lorem Ipsum is simply dummy text of the printing and typesetting</p>
  </div>
  <div class="news-item">
    <div class="news-date"><svg width="22" height="16" aria-hidden="true"><rect x="1" y="1" width="20" height="14" fill="#fff" stroke="#3a5ea8"/><rect x="4" y="4" width="6" height="5" fill="#3a5ea8"/></svg>Date:21 july,2012</div>
    <p>Lorem Ipsum is simply dummy text of the printing and typesetting indus-<br>try&nbsp; Lorem Ipsum is simply dummy text of the printing and typesetting</p>
  </div>
</aside>

<footer class="site-footer">
  <div class="foot-col testimonial" style="left:28px;width:350px">
    <h3>Testimonial</h3>
    <p>Lorem Ipsum is simply dummy text of the printing and typesetting industry&nbsp; Lorem Ipsum is simply dummy text of the printing and typesetting</p>
    <cite>- Marla Venn</cite>
    <p>Lorem Ipsum is simply dummy text of the printing and typesetting industry&nbsp; Lorem Ipsum is simply dummy text of the printing and typesetting</p>
    <cite>- Marla Venn</cite>
  </div>
  <div class="divider" style="left:390px"></div>
  <div class="foot-col payment" style="left:421px;width:300px">
    <h3>Payment Option</h3>
    <div class="cards">
      <span class="card" style="background:#cfd8e6" aria-label="Quibpay"></span>
      <span class="card" style="background:#e7e9f2" aria-label="Zanto"></span>
      <span class="card" style="background:#d9d9d9" aria-label="Fundline"></span>
    </div>
    <div class="action">
      <svg width="30" height="34" aria-hidden="true"><rect x="3" y="2" width="24" height="30" fill="#eef2f6" stroke="#8aa"/><path d="M8 10h14M8 16h14M8 22h10" stroke="#5a7ba8" stroke-width="2"/></svg>
      <div>Like “cartNest” ORDER NOW<br><a href="#">Click here to fill order form</a></div>
    </div>
    <div class="action">
      <svg width="30" height="34" aria-hidden="true"><rect x="3" y="2" width="24" height="30" fill="#f5ecd6" stroke="#b89"/><path d="M8 10h14M8 16h14M8 22h10" stroke="#d07a1a" stroke-width="2"/></svg>
      <div>Make your Payment to easy way - <a href="#">payment FORM</a></div>
    </div>
  </div>
  <div class="divider" style="left:740px"></div>
  <div class="foot-col contact" style="left:778px;top:32px;width:320px">
    <div class="contact-row"><svg width="32" height="34" aria-hidden="true"><rect x="4" y="2" width="24" height="30" rx="2" fill="#3b6fb0"/><circle cx="16" cy="17" r="7" fill="none" stroke="#fff" stroke-width="2"/></svg><span>Suite 210, 4482 Harrow Lane,<br>Elm District, Oakvale</span></div>
    <div class="contact-row"><svg width="34" height="30" aria-hidden="true"><rect x="2" y="6" width="30" height="20" fill="#eef1f4" stroke="#9ab"/><path d="M2 6l15 12 15-12" fill="none" stroke="#c33" stroke-width="2"/></svg><a href="#">info@cartnest.example</a></div>
    <div class="contact-row"><svg width="34" height="34" aria-hidden="true"><rect x="1" y="1" width="32" height="32" rx="6" fill="#5aa83a"/><path d="M11 9c-2 2-1 7 4 12s10 6 12 4l-3-4-3 2c-2-1-5-4-6-6l2-3z" fill="#fff"/></svg><span class="contact-phone">+0149036617250</span></div>
  </div>
</footer>
<div class="copyright">Copyright © 2011 cartNest.example</div>
</body>
</html>
```